Real Estate Company needs Stationary.
Business Cards, Letterhead, Envelope Stationary etc...
Real Estate Company needs Stationary. -
Creative Brief
Professional
Tomas Velbrik
Broker
3871 W. Marrowfield Ave., Suite K-214 Marrowfield TX, 75318
1 (866) 514-VKOR (5867)
tomas@vkorhomesllc.example
www.vkorhomesllc.example
We are a real estate company looking for a slick contemporary design. Use logo in the design. Use logo colors if desired. Would like Business cards, Letterhead, and Envelope. I would like all the stationary items to carry the same theme my logo protrays. Email me with questions.
I would like the logo on back, and open to any other sugestions.

```html
<!DOCTYPE html>
<html lang="en">
<head>
<meta charset="utf-8">
<title>vKorHomes Stationery</title>
<link href="https://fonts.googleapis.com/css2?family=Roboto:wght@400;500;700&display=swap" rel="stylesheet">
<style>
:root{
  --board:#a7a8aa;
  --paper:#ffffff;
  --paper-shade:#eceeef;
  --blue:#1d7cc0;
  --blue-dark:#145f99;
  --green:#5aa83a;
  --ink:#4a4d50;
  --muted:#7a7d80;
}
*{box-sizing:border-box;margin:0;padding:0}
html,body{width:1200px;height:677px;overflow:hidden}
body{background:var(--board);font-family:"Roboto",Arial,sans-serif;color:var(--ink);position:relative}
.sheet{position:absolute;background:linear-gradient(135deg,var(--paper) 40%,var(--paper-shade));box-shadow:1px 2px 4px rgba(0,0,0,.25);overflow:hidden}
.band-top{position:absolute;left:0;right:0;top:0;height:9px;background:linear-gradient(90deg,var(--blue-dark),var(--blue))}
.band-top::after{content:"";position:absolute;left:0;right:0;top:9px;height:3px;background:var(--green)}
.band-bottom{position:absolute;left:0;right:0;bottom:0;height:9px;background:linear-gradient(90deg,var(--blue-dark),var(--blue))}
.band-bottom::before{content:"";position:absolute;left:0;right:0;top:-3px;height:3px;background:var(--green)}
.brand{position:absolute;display:flex;align-items:center;gap:6px;color:var(--blue);font-weight:700;white-space:nowrap}
.brand .mark{display:block;background:var(--green)}
.small{position:absolute;font-size:6.5px;line-height:1.45;color:var(--muted);white-space:nowrap}

/* letterhead */
.letterhead{left:211px;top:48px;width:382px;height:612px}
.letterhead .brand{left:26px;top:48px;font-size:27px}
.letterhead .brand .mark{width:14px;height:14px}
.letterhead .web{right:24px;top:30px}
.letterhead .address{left:26px;bottom:30px}
.letterhead .email{right:24px;bottom:30px}

/* business cards */
.card{left:43px;width:149px;height:92px}
.card-back{top:233px}
.card-back .brand{left:0;right:0;top:36px;justify-content:center;font-size:19px}
.card-back .brand .mark{width:10px;height:10px}
.card-back .web{right:8px;top:16px}
.card-front{top:332px}
.card-front .brand{left:0;right:0;top:18px;justify-content:center;font-size:12px}
.card-front .brand .mark{width:7px;height:7px}
.card-front .person{left:43px;top:38px}
.card-front .person b{display:block;color:var(--blue);font-size:7.5px;font-weight:500}
.card-front .contact{left:8px;top:58px;font-size:5.5px}

/* envelope back */
.envelope-back{left:631px;top:96px;width:526px;height:218px}
.envelope-back svg{position:absolute;left:0;top:0}
.envelope-back .brand{left:0;right:0;top:40px;justify-content:center;font-size:19px}
.envelope-back .brand .mark{width:10px;height:10px}

/* envelope front */
.envelope-front{left:631px;top:372px;width:526px;height:240px}
.envelope-front .brand{left:36px;top:64px;font-size:34px}
.envelope-front .brand .mark{width:16px;height:16px}
.envelope-front .address{left:36px;top:118px}
.envelope-front .email{right:24px;bottom:26px}
</style>
</head>
<body>

<section class="sheet letterhead" aria-label="Letterhead">
  <div class="band-top"></div>
  <div class="brand"><span class="mark"></span>vKorHomes</div>
  <p class="small web">www.vkorhomesllc.example</p>
  <p class="small address">3871 W. Marrowfield Ave., Suite K-214<br>Marrowfield TX, 75318<br>Phone 1 (866) 514-VKOR (5867)<br>Direct (817) 555-0142<br>Fax (817) 555-0199</p>
  <p class="small email">tomas@vkorhomesllc.example</p>
  <div class="band-bottom"></div>
</section>

<section class="sheet card card-back" aria-label="Business card back">
  <div class="band-top"></div>
  <p class="small web">www.vkorhomesllc.example</p>
  <div class="brand"><span class="mark"></span>vKorHomes</div>
  <div class="band-bottom"></div>
</section>

<section class="sheet card card-front" aria-label="Business card front">
  <div class="band-top"></div>
  <div class="brand"><span class="mark"></span>vKorHomes</div>
  <p class="small person"><b>Tomas Velbrik</b>Broker</p>
  <p class="small contact">tomas@vkorhomesllc.example<br>3871 W. Marrowfield Ave., Suite K-214<br>Marrowfield TX, 75318<br>Phone 1 (866) 514-VKOR (5867)<br>Fax (817) 555-0199</p>
  <div class="band-bottom"></div>
</section>

<section class="sheet envelope-back" aria-label="Envelope back">
  <svg width="526" height="218" viewBox="0 0 526 218" aria-hidden="true">
    <path d="M0 0 L236 112 Q263 124 290 112 L526 0" fill="none" stroke="#c9cbcd" stroke-width="1.2"/>
    <path d="M0 218 L232 150 Q263 142 294 150 L526 218" fill="none" stroke="#dcdee0" stroke-width="1"/>
  </svg>
  <div class="brand"><span class="mark"></span>vKorHomes</div>
</section>

<section class="sheet envelope-front" aria-label="Envelope front">
  <div class="band-top"></div>
  <div class="brand"><span class="mark"></span>vKorHomes</div>
  <p class="small address">3871 W. Marrowfield Ave., Suite K-214<br>Marrowfield TX, 75318<br>Phone 1 (866) 514-VKOR (5867)<br>Direct (817) 555-0142<br>Fax (817) 555-0199</p>
  <p class="small email">tomas@vkorhomesllc.example</p>
  <div class="band-bottom"></div>
</section>

</body>
</html>
```